Quiet Hollow Journals - Book Covers - Ebook, Paperback, Hardcover

Title would be:
Quiet Hollow Journals
Subtitle: 9 Simple Steps Including, Site Selection, Pollination and Fertilization, Pruning, Small Spaces, Pest Control, Tropical Fruit Trees, and Berries
Author: Marguerite Olundvale
I would like the designer to have a couple of beautiful pictures on the cover. Please make it unique.
This would be posted on Brindlo so please use specifications for book covers on Brindlo
Back Cover should read:
Quiet Hollow Journals
9 Simple Steps Including, Site Selection, Pollination and Fertilization, Pruning, Small Spaces, Pest Control, Tropical Fruit Trees, and Berries
Marguerite Olundvale
How to grow a thriving orchard and reap a bountiful harvest in less than a year – in both urban and non-urban settings
Fruit trees are fun to grow and will reward you with years of fresh, juicy homegrown produce.
However, the process can be excruciating, especially if you don’t know the best varieties to grow or how to control pests and diseases.
With a little planning and guidance, you will soon be biting into mellow fruits from trees in your backyard – including cherries, plums, pears, apples, and more.
All you need is to learn how to care for the trees, which you will find inside.
In Quiet Hollow Journals, you’ll discover:
● How to pick the right fruit tree varieties for your growing zone and needs to ensure the plants don’t die
● How to effectively plan and prepare the planting site to lay a good foundation for your incoming trees
● How to choose the right irrigation system for your orchard and keep your fruit trees nourished all year long
● Examples of fruit garden plans for different regions – including a guide to help you design your small backyard space
● How to plant fruits to ensure proper pollination, fertilization, and flourishing growth of your produce
● Different fruit tree propagation methods with step-by-step instructions to help you grow your trees without spending money on costly grafts
● When and how to harvest fruits to ensure you collect them at their best and prevent wasting your hard work
● How to boost fruit production, encourage growth, and protect your trees from dangerous diseases
● How to look after fruit trees during all seasons, practice organic farming, and control pests in your garden
And much more…
It’s time to grow your mini-orchard and bask in years of harvest and sweetness from your labor.
Discover how you can have a thriving orchard and a bountiful fruit harvest.
Updates
Hello all Designers,
Please include this on the back cover as I forgot to include it in my main project:
Back Cover to read:
Quiet Hollow Journals
Marguerite Olundvale
And much more…
Target Market(s)
People Who Love Gardening
Industry/Entity Type
Publishing
Requirements
Must have
- Title, Subtitle, Author Name, Beautiful Design, Eye Catching making you want to buy the book
Nice to have
- Large title, Easy to read subtitle intriguing pictures
Should not have
- Busy with too much stuff going on

```html
<!DOCTYPE html>
<html lang="en">
<head>
<meta charset="utf-8">
<title>Quiet Hollow Journals — Front and Back Cover</title>
<link rel="stylesheet" href="https://fonts.googleapis.com/css2?family=EB+Garamond:wght@400;500;700&family=Lato:wght@300;400;700&display=swap">
<style>
  :root {
    --leaf: #76955e;
    --leaf-dark: #5d7d47;
    --berry: #a33443;
    --paper: #ffffff;
    --canvas: #ffffff;
    --ink-light: #f4f1ea;
    --serif: "EB Garamond", Georgia, serif;
    --sans: "Lato", Arial, sans-serif;
  }
  * { box-sizing: border-box; margin: 0; padding: 0; }
  html, body { width: 1200px; height: 1200px; overflow: hidden; background: var(--canvas); }
  .stage { position: relative; width: 1200px; height: 1200px; }

  .cover {
    position: absolute; top: 184px; width: 520px; height: 833px;
    background: var(--leaf); overflow: hidden;
  }
  .cover--front { left: 60px; }
  .cover--back { left: 620px; }

  .band { position: absolute; left: 0; width: 100%; }
  .band--title { background: var(--berry); border-top: 3px solid var(--paper); border-bottom: 3px solid var(--paper); }
  .band--foot { background: var(--berry); border-top: 3px solid var(--paper); bottom: 0; }

  .blossom {
    position: absolute; border-radius: 50%;
    background: radial-gradient(circle at 50% 50%, #f3e7a6 0 18%, #fbf8ef 30%, rgba(251,248,239,0.85) 55%, rgba(251,248,239,0) 72%);
  }

  .title { position: absolute; left: 0; width: 100%; text-align: center; font-family: var(--serif); color: var(--paper); font-weight: 400; line-height: 1; letter-spacing: -0.01em; }
  .subtitle-rule {
    position: absolute; display: flex; align-items: center; gap: 8px;
    font-family: var(--serif); font-weight: 500; color: var(--leaf); line-height: 1; letter-spacing: 0.02em;
  }
  .subtitle-rule::before, .subtitle-rule::after { content: ""; flex: 1; height: 1.5px; background: var(--paper); }

  /* front */
  .front-art {
    position: absolute; left: 0; top: 280px; width: 100%; height: 502px;
    background:
      radial-gradient(ellipse 130px 110px at 150px 205px, #e2463f 0 60%, rgba(226,70,63,0) 100%),
      radial-gradient(ellipse 90px 80px at 90px 260px, #d94848 0 55%, rgba(217,72,72,0) 100%),
      linear-gradient(180deg, #bcd4d6 0%, #3f6b2c 18%, #2f5a24 55%, #7fa255 82%, #9dbb6d 100%);
  }

  .steps {
    position: absolute; background: var(--leaf); border: 2.5px solid var(--paper);
    text-align: center;
  }
  .steps__badge {
    position: absolute; left: 50%; transform: translateX(-50%);
    border-radius: 50%; background: var(--paper);
    display: flex; align-items: center; justify-content: center;
    font-family: var(--serif); font-weight: 700; color: var(--berry); line-height: 1;
  }
  .steps__lead { font-family: var(--sans); color: var(--berry); font-weight: 400; line-height: 1; }
  .steps__list { list-style: none; }
  .steps__list li { font-family: var(--serif); color: var(--paper); line-height: 1; border-bottom: 1px solid var(--berry); }
  .steps__list li:last-child { border-bottom: none; }

  .front-steps { left: 299px; top: 417px; width: 189px; height: 370px; border-bottom: none; padding-top: 54px; }
  .front-steps .steps__badge { top: -40px; width: 70px; height: 70px; font-size: 54px; }
  .front-steps .steps__lead { font-size: 20px; }
  .front-steps .steps__lead--wide { font-size: 21px; letter-spacing: 0.16em; margin-top: 10px; }
  .front-steps .steps__list { margin: 8px 12px 0; }
  .front-steps .steps__list li { font-size: 18px; padding: 6px 0 6px; }

  .author {
    position: absolute; left: 0; width: 100%; text-align: center;
    font-family: var(--sans); font-weight: 400; color: var(--paper);
    letter-spacing: 0.24em; font-size: 23px; line-height: 1;
  }

  /* back */
  .back-steps { left: 334px; top: 169px; width: 140px; height: 269px; padding-top: 36px; }
  .back-steps .steps__badge { top: -27px; width: 52px; height: 52px; font-size: 40px; }
  .back-steps .steps__lead { font-size: 14.5px; }
  .back-steps .steps__lead--wide { font-size: 15px; letter-spacing: 0.14em; margin-top: 7px; }
  .back-steps .steps__list { margin: 6px 10px 0; }
  .back-steps .steps__list li { font-size: 13px; padding: 4px 0 5px; }

  .blurb { position: absolute; left: 59px; top: 265px; width: 239px; font-family: var(--sans); font-weight: 300; font-size: 8.3px; line-height: 1.6; color: var(--ink-light); text-align: justify; }
  .blurb p + p, .blurb ul + p { margin-top: 13px; }
  .blurb .blurb__call { font-family: var(--serif); font-weight: 700; font-size: 9.2px; line-height: 1.45; color: var(--berry); }
  .blurb ul { list-style: none; margin-top: 4px; }
  .blurb li { position: relative; padding-left: 10px; margin-bottom: 4px; text-align: justify; }
  .blurb li::before { content: ""; position: absolute; left: 0; top: 5px; width: 3px; height: 3px; border-radius: 50%; background: var(--ink-light); }

  .back-art {
    position: absolute; left: 316px; top: 452px; width: 181px; height: 339px;
    background: linear-gradient(180deg, rgba(93,125,71,0) 0%, rgba(93,125,71,0.45) 50%, rgba(93,125,71,0.25) 100%);
  }
</style>
</head>
<body>
<main class="stage">

  <section class="cover cover--front" aria-label="Front cover">
    <div class="band band--title" style="top:83px;height:197px;"></div>
    <div class="blossom" role="img" aria-label="Illustration of a white fruit blossom with a honeybee" style="left:205px;top:26px;width:110px;height:90px;"></div>
    <h1 class="title" style="top:112px;font-size:88px;">Quiet Hollow</h1>
    <div class="subtitle-rule" style="left:39px;width:442px;top:211px;font-size:38px;">JOURNALS</div>

    <div class="front-art" role="img" aria-label="Painted illustration of two red apples on a leafy branch in front of an apple tree full of fruit"></div>

    <div class="steps front-steps">
      <div class="steps__badge">9</div>
      <p class="steps__lead">SIMPLE STEPS</p>
      <p class="steps__lead steps__lead--wide">INCLUDING</p>
      <ul class="steps__list">
        <li>Site Selection</li>
        <li>Pollination</li>
        <li>Fertilization</li>
        <li>Pruning</li>
        <li>Small Spaces</li>
        <li>Pest Control</li>
        <li>Tropical Fruit Trees</li>
        <li>Berries</li>
      </ul>
    </div>

    <div class="band band--foot" style="height:51px;"></div>
    <p class="author" style="bottom:14px;">MARGUERITE OLUNDVALE</p>
  </section>

  <section class="cover cover--back" aria-label="Back cover">
    <div class="band band--title" style="top:102px;height:109px;"></div>
    <div class="blossom" role="img" aria-label="Illustration of a white fruit blossom with a honeybee" style="left:155px;top:72px;width:58px;height:50px;"></div>
    <h2 class="title" style="left:20px;width:330px;top:122px;font-size:51px;">Quiet Hollow</h2>
    <div class="subtitle-rule" style="left:59px;width:245px;top:173px;font-size:22px;">JOURNALS</div>

    <div class="steps back-steps">
      <div class="steps__badge">9</div>
      <p class="steps__lead">SIMPLE STEPS</p>
      <p class="steps__lead steps__lead--wide">INCLUDING</p>
      <ul class="steps__list">
        <li>Site Selection</li>
        <li>Pollination</li>
        <li>Fertilization</li>
        <li>Pruning</li>
        <li>Small Spaces</li>
        <li>Pest Control</li>
        <li>Tropical Fruit Trees</li>
        <li>Berries</li>
      </ul>
    </div>

    <div class="blurb">
      <p>How to grow a thriving orchard and reap a bountiful harvest in less than a year – in both urban and non-urban settings Fruit trees are fun to grow and will reward you with years of fresh, juicy homegrown produce. However, the process can be excruciating, especially if you don’t know the best varieties to grow or how to control pests and diseases. With a little planning and guidance, you will soon be biting into mellow fruits from trees in your backyard – including cherries, plums, pears, apples, and more.</p>
      <p class="blurb__call">All you need is to learn how to care for the trees, which you will find inside. In Quiet Hollow Journals, you’ll discover:</p>
      <ul>
        <li>How to pick the right fruit tree varieties for your growing zone and needs to ensure the plants don’t die.</li>
        <li>How to effectively plan and prepare the planting site to lay a good foundation for your incoming trees.</li>
        <li>How to choose the right irrigation system for your orchard and keep your fruit trees nourished all year long.</li>
        <li>Examples of fruit garden plans for different regions – including a guide to help you design your small backyard space.</li>
        <li>How to plant fruits to ensure proper pollination, fertilization, and flourishing growth of your produce.</li>
        <li>Different fruit tree propagation methods with step-by-step instructions to help you grow your trees without spending money on costly grafts.</li>
        <li>When and how to harvest fruits to ensure you collect them at their best and prevent wasting your hard work.</li>
        <li>How to boost fruit production, encourage growth, and protect your trees from dangerous diseases.</li>
        <li>How to look after fruit trees during all seasons, practice organic farming, and control pests in your garden.</li>
      </ul>
      <p class="blurb__call">And much more… It’s time to grow your mini-orchard and bask in years of harvest and sweetness from your labor. Discover how you can have a thriving orchard and a bountiful fruit harvest.</p>
    </div>

    <div class="back-art" role="img" aria-label="Faint line sketch of two young pruned fruit tree saplings"></div>

    <div class="band band--foot" style="height:53px;"></div>
  </section>

</main>
</body>
</html>
```